Energy Healing for pregnant women postcard

I am an intuitive energy healer specializing in the care of pregnant women and their babies. I have an existing logo that is attached that should be placed on the card,sizing is at your discretion, recolor as needed. The message of the card should be one that conveys tranquility, growth, life and light. Images of pregnancy and motherhood could also fit well on the card, but that is not required if the preceding messages can be conveyed through other imagery. Also on the card, the following should appear: (company name and tag line)Positivity & JoyHealing the mind, body, spirit and soul with Energy provided to all living things by the Universe. Space should be left for my name and credentials on the front, while the address space on the back will be used for more contact information. Opposite the address block on the back, please leave room for a text box that will include benefits of the services. About 2"x3" should suffice.

Target Market(s)

Pregnant women and newly post-partum women

Industry/Entity Type

Health And Wellness

Font styles to use
Script

Colors
b05ba4
b768aa
d3a5cc
ecdaeb
e7f5f8
cfdeed
cee9f5
85cae6

Requirements
Must have
• Company logo. Company name. Tag line. Individual name and certifications
Nice to have
• Pictures or images that convey peace, tranquility healing and growth.
Should not have
• Anything harsh.

```html
<!DOCTYPE html>
<html lang="en">
<head>
<meta charset="utf-8">
<title>Harbor &amp; Wren – Energy Healing Postcard</title>
<link href="https://fonts.googleapis.com/css2?family=Cormorant+Garamond:ital,wght@0,500;0,600;1,500;1,600&family=Roboto+Condensed:wght@700&display=swap" rel="stylesheet">
<style>
  :root {
    --page: #ffffff;
    --band: #a05ea0;
    --band-edge: #b768aa;
    --white: #ffffff;
    --plum: #7a1f7c;
    --orchid: #b05ba4;
    --blue-script: #2b5fd8;
    --shadow: rgba(40, 40, 60, 0.35);
  }
  * { margin: 0; padding: 0; box-sizing: border-box; }
  html, body { width: 798px; height: 1200px; overflow: hidden; background: var(--page); }
  .canvas { position: relative; width: 798px; height: 1200px; }

  .card { position: absolute; overflow: hidden; box-shadow: 6px 10px 14px var(--shadow); }
  .card--front { left: 35px; top: 30px; width: 707px; height: 545px; }
  .card--back { left: 30px; top: 606px; width: 709px; height: 540px; background: var(--white); }

  /* Front */
  .front-art {
    position: absolute; inset: 0;
    background:
      radial-gradient(ellipse 120px 60px at 420px 175px, rgba(255, 230, 150, 0.9), transparent 70%),
      linear-gradient(180deg, #3c4f9e 0%, #6f5fae 18%, #e8b86a 33%, #5a3f8c 45%, #3b3f8f 70%, #6b4a9c 100%);
  }
  .front-band {
    position: absolute; left: 0; top: 50px; width: 100%; height: 115px;
    background: var(--band); border-bottom: 3px solid var(--band-edge);
  }
  .brand-mark {
    display: flex; align-items: center; gap: 9px; white-space: nowrap;
    font-family: "Cormorant Garamond", serif; font-weight: 600; color: var(--white);
  }
  .brand-mark__dot { width: 12px; height: 12px; border-radius: 50%; background: var(--white); flex: none; }
  .card--front .brand-mark { position: absolute; left: 30px; top: 88px; font-size: 29px; }
  .tagline {
    position: absolute; left: 259px; top: 53px; width: 440px; white-space: nowrap;
    font-family: "Cormorant Garamond", serif; font-style: italic; font-weight: 500;
    font-size: 26px; line-height: 36px; color: var(--white);
  }
  .credentials {
    position: absolute; left: 40px; top: 388px;
    font-family: "Roboto Condensed", sans-serif; font-weight: 700;
    color: var(--white); font-size: 18px; line-height: 23px; letter-spacing: 0.6px;
  }
  .credentials__name { font-size: 24px; font-variant: small-caps; line-height: 28px; letter-spacing: 0.5px; }

  /* Back */
  .back-photo {
    position: absolute; left: 0; top: 0; width: 370px; height: 100%;
    background: linear-gradient(100deg, #ffffff 0%, #e9e9e9 35%, #cfcfcf 60%, #f2f2f2 100%);
  }
  .benefits { position: absolute; left: 43px; top: 38px; }
  .benefits__title {
    font-family: "Cormorant Garamond", serif; font-style: italic; font-weight: 600;
    font-size: 28px; line-height: 34px; color: var(--blue-script); margin-bottom: 0;
  }
  .benefits__list { list-style: none; font-family: "Roboto Condensed", sans-serif; font-weight: 700; font-size: 22px; color: var(--plum); }
  .benefits__list li { position: relative; padding-left: 28px; line-height: 27px; margin-bottom: 6px; white-space: nowrap; }
  .benefits__list li::before { content: "✦"; position: absolute; left: 0; top: 0; font-size: 18px; }

  .back-contact { position: absolute; left: 364px; top: 0; width: 330px; text-align: center; }
  .back-contact .brand-mark {
    justify-content: center; margin-top: 90px;
    color: var(--orchid); font-size: 38px; line-height: 46px;
  }
  .back-contact .brand-mark__dot { background: var(--orchid); }
  .invite {
    margin-top: 88px; font-family: "Cormorant Garamond", serif; font-style: italic;
    font-weight: 500; font-size: 21px; line-height: 24px; color: var(--blue-script); white-space: nowrap;
  }
  .back-name {
    margin-top: 17px; font-family: "Roboto Condensed", sans-serif; font-weight: 700;
    font-size: 23px; line-height: 26px; font-variant: small-caps; color: var(--plum); white-space: nowrap;
  }
  .back-titles {
    margin-top: 2px; font-family: "Cormorant Garamond", serif; font-style: italic; font-weight: 600;
    font-size: 24px; line-height: 27px; color: var(--blue-script); white-space: nowrap;
  }
  .contact-lines {
    margin-top: 19px; font-family: "Roboto Condensed", sans-serif; font-weight: 700;
    color: var(--plum); font-size: 18px; line-height: 22px; letter-spacing: 0.3px;
  }
  .contact-lines__phone { font-size: 20.5px; line-height: 24px; }
  .rule { display: block; margin: 31px auto 0; }
</style>
</head>
<body>
<main class="canvas">

  <section class="card card--front">
    <div class="front-art" role="img" aria-label="Luminous painting of a kneeling woman wrapped in flowing waves of violet, blue and golden light"></div>
    <div class="front-band"></div>
    <div class="brand-mark"><span class="brand-mark__dot"></span>Harbor &amp; Wren</div>
    <p class="tagline">Healing the mind, body, spirit and soul<br>with Energy provided to all living<br>things by the Universe.</p>
    <div class="credentials">
      <div class="credentials__name">Miriam K. Ellison</div>
      <div>MSN, RCMT</div>
      <div>Reiki Master Teacher</div>
      <div>Archangelic Light Master Teacher</div>
    </div>
  </section>

  <section class="card card--back">
    <div class="back-photo" role="img" aria-label="Soft black and white photo of a pregnant belly cradled by hands, with a pink paper heart"></div>
    <div class="benefits">
      <h2 class="benefits__title">Benefits of Energy Healing</h2>
      <ul class="benefits__list">
        <li>Deep relaxation</li>
        <li>Decrease anxiety</li>
        <li>Decrease stress</li>
        <li>Decrease discomforts</li>
        <li>Promote feelings of<br>wellbeing</li>
        <li>Promote balance</li>
        <li>Relieve physical discomforts<br>of pregnancy</li>
      </ul>
    </div>
    <div class="back-contact">
      <div class="brand-mark"><span class="brand-mark__dot"></span>Harbor &amp; Wren</div>
      <p class="invite">To receive nurturing Energy to sustain<br>ease during pregnancy and beyond call:</p>
      <p class="back-name">Miriam K. Ellison, msn, rcmt</p>
      <p class="back-titles">Reiki Master Teacher,<br>Archangelic Light Master Teacher</p>
      <div class="contact-lines">
        <div class="contact-lines__phone">555-014-2273</div>
        <div>hello@harborandwren.com</div>
        <div>www.harborandwren.com</div>
      </div>
      <svg class="rule" width="130" height="8" viewBox="0 0 130 8" aria-hidden="true">
        <path d="M0 4 Q65 1 130 4 Q65 7 0 4 Z" fill="#2b5fd8"/>
      </svg>
    </div>
  </section>

</main>
</body>
</html>
```